Marlow Crest Group (Real Estate and Investment)

A high end, clean design.
We are a real estate company with sales, asset management and investment divisions. We want to use a black and white scheme which is really high end feel. The back of the card can just be the logo (black background with the white writing) as we will probably emboss this when we print)

Target Market(s)

High level investors, high end houses for sale

Industry/Entity Type

Business

Contact Information for Business Card

Name, position, phone number and email address
Glen Varley, Managing Director, 0437259064 and glen@marlowcrest-example.com.au

Requirements
Must have
• Back of the card to be the black background with the white writing (as per the attached images). Would like the capacity to emboss the writing and logo

```html
<!DOCTYPE html>
<html lang="en">
<head>
<meta charset="utf-8">
<title>Marlow Crest Group – Business Card</title>
<link rel="stylesheet" href="https://fonts.googleapis.com/css2?family=Raleway:wght@400&family=Arimo:wght@400;700&display=swap">
<style>
  :root {
    --ink: #111111;
    --paper: #f4f4f4;
    --card-white: #ffffff;
    --card-black: #050505;
    --reverse: #ffffff;
    --muted: #333333;
  }
  * { margin: 0; padding: 0; box-sizing: border-box; }
  html, body {
    width: 1198px;
    height: 1200px;
    overflow: hidden;
    background: var(--paper);
  }
  .sheet {
    width: 1198px;
    height: 1200px;
    display: flex;
    flex-direction: column;
    align-items: center;
    justify-content: center;
    gap: 60px;
  }
  .card {
    position: relative;
    width: 840px;
    height: 514px;
    box-shadow: 0 2px 10px rgba(0,0,0,0.12);
    overflow: hidden;
  }

  /* Front */
  .card--front { background: var(--card-white); color: var(--ink); }
  .brand {
    position: absolute;
    left: 70px;
    top: 150px;
    width: 300px;
    display: flex;
    flex-direction: column;
    align-items: center;
    gap: 26px;
  }
  .brand__circle {
    width: 120px;
    height: 120px;
    border: 2px solid var(--ink);
    border-radius: 50%;
  }
  .brand__name {
    font-family: "Raleway", sans-serif;
    font-weight: 400;
    font-size: 27px;
    letter-spacing: 0.5px;
    text-transform: uppercase;
    white-space: nowrap;
    color: var(--ink);
  }
  .contact {
    position: absolute;
    left: 470px;
    top: 104px;
    font-family: "Arimo", sans-serif;
  }
  .contact__name {
    font-weight: 700;
    font-size: 30px;
    font-variant: small-caps;
    letter-spacing: 0.5px;
  }
  .contact__role {
    font-size: 19px;
    font-variant: small-caps;
    color: var(--muted);
    margin-top: 4px;
  }
  .contact__list {
    list-style: none;
    margin-top: 88px;
    display: flex;
    flex-direction: column;
    gap: 14px;
  }
  .contact__item {
    display: flex;
    align-items: center;
    gap: 10px;
    font-size: 18px;
    font-variant: small-caps;
    color: var(--ink);
  }
  .contact__icon { width: 18px; height: 18px; flex: none; }

  /* Back */
  .card--back { background: var(--card-black); }
  .back__circle {
    position: absolute;
    left: -160px;
    top: -40px;
    width: 540px;
    height: 540px;
    border: 6px solid var(--reverse);
    border-radius: 50%;
  }
  .back__name {
    position: absolute;
    right: 36px;
    top: 296px;
    font-family: "Raleway", sans-serif;
    font-weight: 400;
    font-size: 32px;
    letter-spacing: 0.5px;
    text-transform: uppercase;
    white-space: nowrap;
    color: var(--reverse);
  }
</style>
</head>
<body>
<main class="sheet">

  <section class="card card--front" aria-label="Card front">
    <div class="brand">
      <div class="brand__circle"></div>
      <div class="brand__name">Marlow Crest Group</div>
    </div>
    <div class="contact">
      <div class="contact__name">Glen Varley</div>
      <div class="contact__role">Managing Director</div>
      <ul class="contact__list">
        <li class="contact__item">
          <svg class="contact__icon" viewBox="0 0 18 18" aria-hidden="true">
            <rect x="5" y="1" width="8" height="16" rx="1.5" fill="none" stroke="#111" stroke-width="1.6"/>
            <line x1="8" y1="14.5" x2="10" y2="14.5" stroke="#111" stroke-width="1.4"/>
          </svg>
          <span>043.725.9064</span>
        </li>
        <li class="contact__item">
          <svg class="contact__icon" viewBox="0 0 18 18" aria-hidden="true">
            <rect x="1" y="4" width="16" height="11" fill="#111"/>
            <polyline points="1,4 9,10.5 17,4" fill="none" stroke="#fff" stroke-width="1.3"/>
          </svg>
          <span>glen@marlowcrest-example.com.au</span>
        </li>
        <li class="contact__item">
          <svg class="contact__icon" viewBox="0 0 18 18" aria-hidden="true">
            <circle cx="9" cy="9" r="7.5" fill="none" stroke="#111" stroke-width="1.5"/>
            <ellipse cx="9" cy="9" rx="3.3" ry="7.5" fill="none" stroke="#111" stroke-width="1.2"/>
            <line x1="1.5" y1="9" x2="16.5" y2="9" stroke="#111" stroke-width="1.2"/>
          </svg>
          <span>marlowcrest-example.com.au</span>
        </li>
      </ul>
    </div>
  </section>

  <section class="card card--back" aria-label="Card back">
    <div class="back__circle"></div>
    <div class="back__name">Marlow Crest Group</div>
  </section>

</main>
</body>
</html>
```